Pembrook Nightclub Flyer Grand Opening

Grand Opening Teaser Flyer For Nightclub

Text for flyer:
PEMBROOK
Nightclub + Lounge
Opening Fall 2018
Downtown Sacramento
Now Hiring (All Positions)
www.pembrookvenue.example
Powered by HALM Acoustics

Email Resume to: club@pembrookvenue.example

Target Market(s)

Upscale Nightclub and Lounge

Industry/Entity Type

Night Club

Font styles to use
Sans Serif

Colors
9ccb3b
0393ce
0355a3
b2b2b2
000000

Requirements
Must have
• Vibrant colors like the flyer example, and our logo. For use on Facebook and Instagram, will be boosted as well.
Nice to have
• Something artsy like the flyer example but not required

```html
<!DOCTYPE html>
<html lang="en">
<head>
<meta charset="utf-8">
<title>Pembrook Nightclub – Grand Opening Flyer</title>
<link rel="stylesheet" href="https://fonts.googleapis.com/css2?family=Jost:wght@400;500;600&display=swap">
<style>
  :root {
    --lime: #9ccb3b;
    --lime-bright: #d8f56a;
    --cyan: #0393ce;
    --royal: #0355a3;
    --ice: #c9ecff;
    --silver: #b2b2b2;
    --ink: #000000;
    --stage: #eeeff0;
    --white: #ffffff;
  }
  html, body {
    margin: 0;
    width: 1200px;
    height: 923px;
    overflow: hidden;
    background: var(--stage);
    font-family: "Jost", Arial, sans-serif;
  }
  .flyer {
    position: absolute;
    left: 320px;
    top: 30px;
    width: 560px;
    height: 862px;
    overflow: hidden;
    background: var(--ink);
    text-align: center;
  }
  .flyer__scene {
    position: absolute;
    inset: 0;
    background:
      radial-gradient(ellipse 45% 30% at 50% 34%, rgba(80, 90, 230, 0.75), transparent 70%),
      radial-gradient(ellipse 60% 25% at 30% 48%, rgba(150, 40, 60, 0.45), transparent 75%),
      radial-gradient(ellipse 70% 35% at 50% 20%, rgba(3, 85, 163, 0.8), transparent 75%),
      linear-gradient(180deg, #050818 0%, #0a0f3a 30%, #1a0b24 58%, #050505 75%, #000 100%);
  }
  .flyer__speakers {
    position: absolute;
    left: 30px;
    right: 30px;
    bottom: 0;
    height: 250px;
    border-radius: 30px 30px 0 0;
    background:
      radial-gradient(circle at 18% 55%, rgba(3, 147, 206, 0.55), transparent 30%),
      radial-gradient(circle at 82% 55%, rgba(3, 147, 206, 0.55), transparent 30%),
      radial-gradient(circle at 50% 60%, rgba(3, 85, 163, 0.7), transparent 40%),
      linear-gradient(180deg, #0b1a33 0%, #06101f 100%);
  }
  .flyer__line {
    position: absolute;
    left: 0;
    right: 0;
    margin: 0;
    line-height: 1;
  }
  .headline {
    font-weight: 400;
    font-size: 104px;
    color: var(--ice);
    text-shadow: 0 0 6px var(--cyan), 0 0 16px var(--cyan), 0 0 28px var(--royal);
  }
  .headline--grand { top: 3px; }
  .headline--opening { top: 90px; }
  .season {
    top: 185px;
    font-size: 58px;
    font-weight: 400;
    color: var(--ice);
    text-shadow: 0 0 6px var(--cyan), 0 0 14px var(--royal);
  }
  .brand-name {
    top: 410px;
    font-size: 46px;
    font-weight: 500;
    letter-spacing: 0.62em;
    padding-left: 0.62em;
    color: var(--lime-bright);
  }
  .venue-type {
    top: 480px;
    font-size: 23px;
    font-weight: 600;
    letter-spacing: 0.42em;
    padding-left: 0.42em;
    color: var(--lime-bright);
    text-shadow: 0 0 8px rgba(156, 203, 59, 0.7);
  }
  .location {
    top: 526px;
    font-size: 24px;
    font-weight: 500;
    color: var(--lime-bright);
    text-shadow: 0 0 8px rgba(156, 203, 59, 0.6);
  }
  .hiring {
    top: 590px;
    font-size: 30px;
    font-weight: 500;
    color: var(--white);
  }
  .website {
    top: 644px;
    font-size: 23px;
    font-weight: 600;
    color: var(--white);
    text-shadow: 0 0 6px rgba(0, 0, 0, 0.9);
  }
  .apply {
    top: 684px;
    font-size: 17px;
    font-weight: 600;
    line-height: 1.15;
    color: var(--white);
    text-shadow: 0 0 6px rgba(0, 0, 0, 0.9);
  }
  .sponsor-label {
    top: 754px;
    font-size: 17px;
    font-weight: 600;
    color: var(--cyan);
  }
  .sponsor-name {
    top: 784px;
    font-size: 34px;
    font-weight: 500;
    color: var(--cyan);
  }
</style>
</head>
<body>
  <main class="flyer">
    <div class="flyer__scene" role="img" aria-label="Neon-lit club interior with a dancer silhouette and blue lightning"></div>
    <div class="flyer__speakers" role="img" aria-label="Stack of glowing loudspeakers"></div>

    <h1 class="flyer__line headline headline--grand">GRAND</h1>
    <h1 class="flyer__line headline headline--opening">OPENING</h1>
    <p class="flyer__line season">FALL 2018</p>

    <p class="flyer__line brand-name">PEMBROOK</p>
    <p class="flyer__line venue-type">NIGHTCLUB &amp; LOUNGE</p>
    <p class="flyer__line location">DOWNTOWN SACRAMENTO</p>

    <p class="flyer__line hiring">NOW HIRING (ALL POSITIONS)</p>
    <p class="flyer__line website">WWW.PEMBROOKVENUE.EXAMPLE</p>
    <p class="flyer__line apply">EMAIL RESUME TO:<br>CLUB@PEMBROOKVENUE.EXAMPLE</p>

    <p class="flyer__line sponsor-label">Powered by</p>
    <p class="flyer__line sponsor-name">HALM ACOUSTICS</p>
  </main>
</body>
</html>
```